Business card design for a world class martial arts and group fitness facility

We need a professional and eye catching design for a business card. The card will be used in networking as well as marketing.
We are a martial arts facility offering Taekwondo, Brazilian Jiu Jitsu, and group fitness. All of our programs are geared for kids and adults.
Our Taekwondo program is lead by a Hall of Fame instructor who was Instructor of the Year in 2015.
Our Brazilian Jiu Jitsu program is lead by a wold class instructor who is also a part of the renown Brazilian KVO team.
We offer 3 focused group fitness programs: Ring striking, Pulse Fitness, and The Meadow which are all lead by certified instructors in a small group setting.
Our facility is state of the art and has been recognized as such in nationally published magazines.
Our business is named The Lantern which is the linear logo that is attached. This is the main logo. I also attached a circular logo we have used in some marketing material. Our Jiu Jitsu program is the KVO team logo. The Taekwondo program is the TORVEX Prime. It would be nice to somehow incorporate all 3 logos, but The Lantern is most important.
Industry/Entity Type
Martial Art
Contact Information for Business Card
We would like to use all 3 logos if possible but The Lantern is the most important. We would like to have a place for a staff member's name while keeping the focus on the programs we offer.
Look and feel
Each slider illustrates characteristics of the customer's brand and the style your logo design should communicate.

```html
<!DOCTYPE html>
<html lang="en">
<head>
<meta charset="utf-8">
<title>The Lantern – Business Card</title>
<link href="https://fonts.googleapis.com/css2?family=Crimson+Text:wght@400;600&family=Open+Sans:wght@400;600;800&display=swap" rel="stylesheet">
<style>
  :root {
    --page: #d9d9d9;
    --card: #ffffff;
    --ink: #1a1a1a;
    --brick: #6e2b16;
    --muted: #4a4a4a;
    --rule: #3a3a3a;
    --address: #f1e6e0;
  }
  * { margin: 0; padding: 0; box-sizing: border-box; }
  html, body { width: 1189px; height: 1200px; overflow: hidden; }
  body {
    background: var(--page);
    font-family: "Open Sans", Arial, sans-serif;
    color: var(--ink);
    position: relative;
  }
  .card {
    position: absolute;
    left: 140px;
    width: 917px;
    height: 522px;
    background: var(--card);
    overflow: hidden;
  }
  .card--front { top: 45px; }
  .card--back { top: 601px; }

  /* Front */
  .wordmark {
    position: absolute;
    font-weight: 800;
    color: var(--ink);
    text-transform: uppercase;
    letter-spacing: -1px;
    line-height: 1;
    white-space: nowrap;
  }
  .card--front .wordmark {
    left: 35px; top: 188px;
    font-size: 58px;
  }
  .divider {
    position: absolute;
    left: 460px; top: 55px;
    width: 2px; height: 318px;
    background: var(--rule);
  }
  .staff { position: absolute; left: 490px; top: 72px; }
  .staff__name {
    font-family: "Crimson Text", Georgia, serif;
    font-weight: 600;
    font-size: 50px;
    color: var(--brick);
    line-height: 1;
  }
  .staff__role {
    font-size: 26px;
    color: var(--ink);
    margin-left: 18px;
    margin-top: 2px;
  }
  .contacts {
    position: absolute;
    left: 500px; top: 240px;
    list-style: none;
  }
  .contacts li {
    display: flex;
    align-items: center;
    height: 41px;
    font-size: 25px;
    letter-spacing: 0.5px;
  }
  .contacts svg { width: 22px; height: 22px; margin-right: 35px; flex: none; }
  .swoosh { position: absolute; left: 0; bottom: 0; width: 917px; height: 130px; }
  .address {
    position: absolute;
    left: 0; width: 100%;
    top: 462px;
    text-align: center;
    font-size: 25px;
    color: var(--address);
  }

  /* Back */
  .seal {
    position: absolute;
    left: 271px; top: 60px;
    width: 376px; height: 376px;
    border: 12px solid var(--rule);
    border-radius: 50%;
    display: flex;
    align-items: center;
    justify-content: center;
  }
  .card--back .wordmark {
    position: static;
    font-size: 44px;
    color: var(--rule);
  }
  .program {
    position: absolute;
    display: flex;
    align-items: center;
    gap: 8px;
    font-weight: 800;
    font-size: 17px;
    color: var(--ink);
    text-transform: uppercase;
  }
  .program--left { left: 70px; top: 236px; }
  .program--right { left: 718px; top: 236px; }
  .program__mark {
    width: 22px; height: 22px;
    background: var(--ink);
    flex: none;
  }
  .program__mark--circle { border-radius: 50%; }
</style>
</head>
<body>
  <section class="card card--front" aria-label="Card front">
    <div class="wordmark">The Lantern</div>
    <div class="divider"></div>
    <div class="staff">
      <div class="staff__name">Daniel Marsh</div>
      <div class="staff__role">President</div>
    </div>
    <ul class="contacts">
      <li>
        <svg viewBox="0 0 22 22" aria-hidden="true"><rect width="22" height="22" fill="#6e2b16"/><path d="M7 5c1 0 2 2.5 2 3s-1.2 1-1 2 2.5 3.8 3.5 4 1.3-1 1.8-1 3 1 3 2-1.5 2.2-2.8 2C9 16.5 5.5 13 5 8 4.8 6 6 5 7 5z" fill="#fff"/></svg>
        555 014 2278
      </li>
      <li>
        <svg viewBox="0 0 22 22" aria-hidden="true"><rect width="22" height="22" fill="#6e2b16"/><circle cx="11" cy="11" r="6.5" fill="none" stroke="#fff" stroke-width="1.8"/><path d="M4.5 11h13M11 4.5c-3 3.5-3 9.5 0 13M11 4.5c3 3.5 3 9.5 0 13" fill="none" stroke="#fff" stroke-width="1.2"/></svg>
        www.lanterndojo.com
      </li>
      <li>
        <svg viewBox="0 0 22 22" aria-hidden="true"><rect width="22" height="22" fill="#6e2b16"/><rect x="4" y="6.5" width="14" height="9" fill="#fff"/><path d="M4 6.5l7 5 7-5" fill="none" stroke="#6e2b16" stroke-width="1.3"/></svg>
        hello@lanterndojo.com
      </li>
    </ul>
    <svg class="swoosh" viewBox="0 0 917 130" preserveAspectRatio="none" aria-hidden="true">
      <path d="M60 70 C300 10 700 -5 917 40 L917 75 C740 35 420 35 60 70 Z" fill="#111"/>
      <path d="M0 90 C250 40 650 20 917 85 L917 130 L0 130 Z" fill="#6e2b16"/>
    </svg>
    <div class="address">412 Harlow Glen rd. Millbrook pa 19000 suite 12</div>
  </section>

  <section class="card card--back" aria-label="Card back">
    <div class="program program--left"><span class="program__mark"></span>TORVEX Prime</div>
    <div class="seal">
      <div class="wordmark">The Lantern</div>
    </div>
    <div class="program program--right"><span class="program__mark program__mark--circle"></span>KVO</div>
  </section>
</body>
</html>
```